Meadowlark Learning Growth Partners (MLGP)

This is a professional business card. Logo and picture are a must on the front of the card. I am an educational consultant. I have been consulting for the past three years for a company. I am now opening my own company. My goal for my consulting company is to eventually consult all over America.

Target Market(s)

Educators, schools, professionals

Industry/Entity Type

Consulting

Contact Information for Business Card

Picture/logo on front, simple modern design

Font styles to use
Serif

Colors
85abd2
0355a3
3176b5
cedeed

Requirements
Must have
• picture, logo,
• Odessa Pruitt, Ed.S
• address 5073 Cormorant ridge Dr. Nashville, TN 37940
• Cell:616-555-0148
• Office: 629-555-0172
• www.Mlgpedu.example
• pruittodessa@mailbox.example

```html
<!DOCTYPE html>
<html lang="en">
<head>
<meta charset="utf-8">
<title>Odessa Pruitt, Ed.S — Business Card</title>
<link href="https://fonts.googleapis.com/css2?family=Tinos:wght@400;700&display=swap" rel="stylesheet">
<style>
  :root {
    --navy: #0355a3;
    --title-blue: #2a5aa8;
    --band-light: #6f95d0;
    --band-mid: #4f7dc4;
    --panel-top: #3a6fbf;
    --panel-bottom: #1d55ab;
    --ring: #85abd2;
    --photo-a: #7fa3d6;
    --photo-b: #cedeed;
    --white: #ffffff;
  }
  html, body {
    margin: 0;
    padding: 0;
    width: 1200px;
    height: 686px;
    overflow: hidden;
    background: #ffffff;
  }
  .card {
    position: relative;
    width: 1200px;
    height: 686px;
    overflow: hidden;
    font-family: "Tinos", "Times New Roman", serif;
    color: var(--white);
  }
  .card-background {
    position: absolute;
    inset: 0;
  }
  .brand {
    position: absolute;
    left: 50px;
    top: 70px;
    display: flex;
    align-items: center;
    gap: 12px;
  }
  .brand-dot {
    width: 26px;
    height: 26px;
    border-radius: 50%;
    background: var(--navy);
  }
  .brand-name {
    font-size: 50px;
    font-weight: 700;
    color: var(--navy);
    letter-spacing: 1px;
  }
  .person-name {
    position: absolute;
    left: 271px;
    top: 113px;
    margin: 0;
    font-size: 50px;
    font-weight: 400;
    color: var(--title-blue);
    line-height: 1;
    white-space: nowrap;
  }
  .contact {
    position: absolute;
    left: 54px;
    margin: 0;
    font-size: 34px;
    line-height: 1;
    white-space: nowrap;
  }
  .contact strong { font-weight: 700; }
  .contact-cell { top: 323px; }
  .contact-office { top: 373px; }
  .contact-web { top: 433px; }
  .contact-email { top: 484px; }
  .contact-icon {
    display: inline-block;
    width: 30px;
    height: 30px;
    vertical-align: -4px;
    margin-right: 10px;
  }
  .address {
    position: absolute;
    right: 29px;
    top: 494px;
    margin: 0;
    text-align: right;
    font-size: 37px;
    line-height: 50px;
    font-style: normal;
    white-space: nowrap;
  }
  .address-pin {
    width: 40px;
    height: 50px;
    vertical-align: -8px;
    margin-right: 4px;
  }
</style>
</head>
<body>
  <div class="card">
    <svg class="card-background" width="1200" height="686" viewBox="0 0 1200 686">
      <defs>
        <linearGradient id="bandGradient" x1="0" y1="0" x2="1" y2="1">
          <stop offset="0" stop-color="#5d88ca"/>
          <stop offset="1" stop-color="#4a78c0"/>
        </linearGradient>
        <linearGradient id="panelGradient" x1="0" y1="0" x2="1" y2="1">
          <stop offset="0" stop-color="#3d72c1"/>
          <stop offset="1" stop-color="#1a52a8"/>
        </linearGradient>
        <linearGradient id="photoGradient" x1="0" y1="0" x2="0" y2="1">
          <stop offset="0" stop-color="#8fb0dc"/>
          <stop offset="1" stop-color="#5c82c0"/>
        </linearGradient>
      </defs>
      <rect class="top-area" x="0" y="0" width="1200" height="686" fill="#ffffff"/>
      <polygon class="lower-band" points="0,233 860,233 571,686 0,686" fill="url(#bandGradient)"/>
      <polygon class="right-panel" points="986,0 1200,0 1200,686 571,686 845,233" fill="url(#panelGradient)"/>
      <line class="accent-stripe" x1="806" y1="336" x2="574" y2="686" stroke="#ffffff" stroke-width="5"/>
      <circle class="photo-ring" cx="969" cy="271" r="174" fill="var(--ring)"/>
      <circle class="photo-frame" cx="969" cy="271" r="147" fill="url(#photoGradient)" role="img" aria-label="Portrait photograph of Odessa Pruitt"/>
    </svg>

    <div class="brand">
      <span class="brand-dot"></span>
      <span class="brand-name">MLGP</span>
    </div>

    <h1 class="person-name">Odessa Pruitt, Ed.S</h1>

    <p class="contact contact-cell">Cell: <strong>616-555-0148</strong></p>
    <p class="contact contact-office">Office: <strong>629-555-0172</strong></p>
    <p class="contact contact-web">
      <svg class="contact-icon" viewBox="0 0 30 30" aria-hidden="true">
        <g fill="none" stroke="#ffffff" stroke-width="1.8">
          <circle cx="15" cy="15" r="12"/>
          <ellipse cx="15" cy="15" rx="5.5" ry="12"/>
          <line x1="3" y1="15" x2="27" y2="15"/>
          <line x1="5" y1="9" x2="25" y2="9"/>
          <line x1="5" y1="21" x2="25" y2="21"/>
        </g>
      </svg><strong>www.Mlgpedu.example</strong>
    </p>
    <p class="contact contact-email">
      <svg class="contact-icon" viewBox="0 0 30 30" aria-hidden="true">
        <g fill="none" stroke="#ffffff" stroke-width="1.8">
          <rect x="2" y="6" width="26" height="18"/>
          <polyline points="2,6 15,17 28,6"/>
        </g>
      </svg><strong>pruittodessa@mailbox.example</strong>
    </p>

    <address class="address">
      <svg class="address-pin" viewBox="0 0 40 50" aria-hidden="true">
        <path d="M20 3 C10 3 4 10 4 18 C4 30 20 46 20 46 C20 46 36 30 36 18 C36 10 30 3 20 3 Z" fill="none" stroke="#ffffff" stroke-width="2.5"/>
        <circle cx="20" cy="18" r="6" fill="none" stroke="#ffffff" stroke-width="2.5"/>
      </svg>5073 Cormorant ridge<br>
      Dr. Nashville, TN 37940
    </address>
  </div>
</body>
</html>
```